Quimby's Yard & Garden Center Business Card Update

I need an updated Business card design for my Lawn and Garden Center. We do Landscaping installs, Lawn Mowing, Snow Removal and also have a Garden Center Retail Division. I uploaded a few of our previous business cards to give an idea of what we are starting with. The main goal of this update is to simplify and modernize the business card, not all of the services that are on the previous cards has to be on the new one but I would still like to highlight our main services. There is also a sample of our logo that Can be used in the design.

Industry/Entity Type

Landscaping

Contact Information for Business Card

Morris Quimby
Morris@Quimbysyardandgarden.example
Business (555) 201-7784
Cell (555) 318-6092

Colors

Designer to choose colors to be used in the design.

Requirements
Must have
• Services Provided :
• Landscaping
• Lawn Maintenance
• Snow Removal
• Garden Center

```html
<!DOCTYPE html>
<html lang="en">
<head>
<meta charset="utf-8">
<title>Quimby's Yard &amp; Garden Center – Business Card</title>
<link rel="stylesheet" href="https://fonts.googleapis.com/css2?family=Open+Sans:ital,wght@0,400;0,700;1,600&display=swap">
<style>
  :root {
    --page-bg: #f0f0f2;
    --card-white: #ffffff;
    --sage: #d9e3a6;
    --lime: #adc44a;
    --forest: #23512a;
    --olive: #5f7a35;
    --ink: #111111;
    --text-light: #ffffff;
  }
  html, body {
    margin: 0;
    padding: 0;
    width: 1200px;
    height: 1000px;
    overflow: hidden;
    background: var(--page-bg);
    font-family: "Open Sans", sans-serif;
  }
  .business-card {
    position: absolute;
    left: 292px;
    top: 316px;
    width: 615px;
    height: 342px;
    box-shadow: 0 3px 8px rgba(0, 0, 0, 0.18);
  }
  .business-card svg { display: block; width: 100%; height: 100%; }
  .brand-name { font-weight: 700; fill: var(--forest); }
  .section-title { font-weight: 700; fill: var(--ink); }
  .service-heading { font-weight: 700; fill: var(--ink); }
  .service-item { font-weight: 400; fill: var(--ink); }
  .contact-name { font-style: italic; font-weight: 600; fill: var(--olive); }
  .contact-line { font-weight: 400; fill: var(--text-light); }
  .icon { fill: none; stroke: var(--olive); stroke-width: 2.2; stroke-linecap: round; stroke-linejoin: round; }
  .icon-solid { fill: var(--olive); }
</style>
</head>
<body>
  <div class="business-card">
    <svg viewBox="0 0 1077 598" xmlns="http://www.w3.org/2000/svg" aria-label="Quimby's Yard &amp; Garden Center business card">
      <defs>
        <linearGradient id="hillsTone" x1="0" y1="0" x2="0" y2="1">
          <stop offset="0" stop-color="var(--lime)"/>
          <stop offset="0.12" stop-color="var(--olive)"/>
          <stop offset="0.25" stop-color="var(--forest)"/>
          <stop offset="1" stop-color="var(--forest)"/>
        </linearGradient>
      </defs>

      <rect class="panel-white" width="1077" height="598" fill="var(--card-white)"/>
      <rect class="panel-services" x="645" y="0" width="432" height="372" fill="var(--sage)"/>
      <rect class="hills-area" role="img" aria-label="Decorative rolling green hills" x="0" y="372" width="1077" height="226" fill="url(#hillsTone)"/>

      <!-- brand -->
      <circle class="brand-dot" cx="108" cy="165" r="14" fill="var(--forest)"/>
      <text class="brand-name" x="135" y="190" font-size="74">Quimby's</text>

      <!-- services -->
      <text class="section-title" x="706" y="86" font-size="39">GREENHOUSE</text>
      <rect class="section-rule" x="645" y="109" width="432" height="8" fill="var(--lime)"/>
      <text class="service-heading" x="706" y="168" font-size="36">Services Provided :</text>
      <text class="service-item" x="706" y="214" font-size="34">Landscaping</text>
      <text class="service-item" x="706" y="259" font-size="34">Lawn Maintenance</text>
      <text class="service-item" x="706" y="304" font-size="34">Snow Removal</text>
      <text class="service-item" x="706" y="350" font-size="34">Garden Center</text>

      <!-- contact -->
      <text class="contact-name" x="117" y="436" font-size="38">Morris Quimby</text>

      <path class="icon-solid phone-icon" d="M82,459 C80,461 79,465 82,470 C86,476 91,480 96,481 C99,482 101,480 102,478 L98,474 C97,473 95,474 94,475 C91,474 88,471 87,468 C88,467 89,465 88,464 Z"/>
      <text class="contact-line" x="117" y="482" font-size="34">(555) 201-7784</text>

      <rect class="icon mobile-icon" x="84" y="500" width="15" height="25" rx="3"/>
      <line class="icon" x1="89" y1="520" x2="94" y2="520"/>
      <text class="contact-line" x="117" y="527" font-size="34">(555) 318-6092</text>

      <rect class="icon mail-icon" x="80" y="554" width="25" height="17" rx="1"/>
      <polyline class="icon" points="80,554 92.5,564 105,554"/>
      <text class="contact-line" x="117" y="572" font-size="34">Morris@Quimbysyardandgarden.example</text>
    </svg>
  </div>
</body>
</html>
```